Brightleaf Plots LLC business card

I created a front and back idea of what I want. Also I included my Brightleaf Plots logo to be used on the card. Please use your creativity to make it look professional and awesome! Use the all text and phrases in the sample card that I made.

(Front of card)Key words and phrases:
FOOD GROWING MACHINES
Aeroponics Technology
No soil
No pesticides
98% less water
Grow year round

(Back of card)
EVERY MONTH ONE SPIRE PLANTER WILL BE GIVEN AWAY
FOLLOW US ON IG FOR A CHANCE TO WIN A SPIRE PLANTER
FOOD GROWING MACHINES
Vertical Farming
Urban Farming
100% Organic
Grows 40% Faster
Indoors/outdoors

My contact info:
Chef Morv
Phone:555 417-3290
web: brightleafplots.example
IG: brightleafplotsxy

Target Market(s)

urban farming, vertical farming gardening

Industry/Entity Type

Gardening

Contact Information for Business Card

Front of card)Key words and phrases:
FOOD GROWING MACHINES
Aeroponics Technology
No soil
No pesticides
98% less water
Grow year round

(Back of card)
FOOD GROWING MACHINES
Vertical Farming
Urban Farming
100% Organic
Grows 40% Faster
Indoors/outdoors

My contact info:
Phone:555 417-3290
web: brightleafplots.example
IG: brightleafplotsxy

Requirements
Must have
• My contact info:
Chef Morv
Phone:555 417-3290
web: brightleafplots.example
IG: brightleafplotsxy
Nice to have
• Great imagery and easy to read. Try to incorporate the image that I uploaded of the little girl.

```html
<!DOCTYPE html>
<html lang="en">
<head>
<meta charset="utf-8">
<title>Brightleaf Plots LLC – Business Card</title>
<link rel="stylesheet" href="https://fonts.googleapis.com/css2?family=Archivo:ital,wght@0,400;0,700;0,900;1,800&display=swap">
<style>
  :root {
    --pink: #e0285a;
    --pink-dark: #c81d4c;
    --green: #2f9a3c;
    --leaf: #7cc243;
    --ink: #2b2b2b;
    --paper: #ffffff;
    --backdrop: #dcdcdc;
    --photo-warm: #d9c7b8;
    --photo-cool: #b9c8b0;
  }
  * { box-sizing: border-box; margin: 0; padding: 0; }
  html, body { width: 1200px; height: 675px; overflow: hidden; }
  body {
    background: var(--backdrop);
    font-family: "Archivo", Arial, sans-serif;
    position: relative;
  }

  /* ---------- landscape card ---------- */
  .card { position: absolute; border-radius: 18px; overflow: hidden; background: var(--paper);
          box-shadow: 0 6px 18px rgba(0,0,0,.18); }
  .card--promo { left: 120px; top: 177px; width: 560px; height: 320px; }
  .promo-photo { position: absolute; inset: 0;
    background: linear-gradient(100deg, var(--photo-warm) 0%, #e7d3d6 35%, #d5dccd 60%, var(--photo-cool) 100%); }
  .promo-veil { position: absolute; inset: 0; background: rgba(255,255,255,.62); }
  .band { position: absolute; left: 0; right: 0; background: var(--pink); color: var(--paper);
          font-weight: 800; font-style: italic; text-align: center; letter-spacing: .5px; font-size: 15px;
          display: flex; align-items: center; justify-content: center; }
  .band--top { top: 0; height: 36px; }
  .band--bottom { bottom: 0; height: 44px; }
  .promo-columns { position: absolute; top: 36px; bottom: 44px; left: 0; right: 0; display: flex; }
  .feature { flex: 1; padding: 18px 22px 0 30px; }
  .divider { width: 5px; background: var(--pink); margin: 16px 0 14px; }
  .feature-title { color: var(--green); font-weight: 900; font-size: 23px; line-height: 1.02;
                   text-align: center; letter-spacing: .3px; }
  .feature-sub { color: var(--ink); font-weight: 700; font-size: 16px; text-align: center; margin: 3px 0 8px; }
  .feature-list { list-style: none; padding-left: 6px; }
  .feature-list li { display: flex; align-items: center; gap: 10px; color: var(--ink);
                     font-weight: 700; font-size: 15px; height: 25px; }
  .tick { width: 18px; height: 16px; flex: none; }

  /* ---------- portrait card ---------- */
  .card--contact { left: 760px; top: 57px; width: 320px; height: 560px; }
  .contact-hero { position: absolute; left: 0; top: 0; width: 320px; height: 300px; }
  .brand { position: absolute; right: 30px; top: 294px; display: flex; align-items: center; gap: 10px; }
  .brand-name { color: var(--leaf); font-weight: 900; font-size: 32px; line-height: .95; text-align: right;
                text-transform: uppercase; }
  .brand-dot { width: 20px; height: 20px; border-radius: 50%; background: var(--leaf); flex: none; }
  .person { position: absolute; right: 30px; top: 376px; text-align: right; }
  .person-name { color: var(--pink); font-weight: 900; font-size: 26px; text-transform: uppercase; }
  .person-role { color: var(--leaf); font-weight: 700; font-size: 11px; text-transform: uppercase; margin-top: 1px; }
  .contact-list { position: absolute; left: 30px; top: 446px; list-style: none; }
  .contact-list li { display: flex; align-items: center; gap: 8px; color: var(--ink); font-weight: 700;
                     font-size: 16px; height: 30px; }
  .contact-icon { width: 16px; height: 16px; flex: none; }
  .contact-label { color: var(--pink); font-weight: 900; font-size: 16px; }
</style>
</head>
<body>

<section class="card card--promo" aria-label="Promotional side of business card">
  <div class="promo-photo" role="img" aria-label="Photo of a young girl in a pink shirt harvesting leafy greens in a kitchen"></div>
  <div class="promo-veil"></div>
  <div class="band band--top">EVERY MONTH ONE SPIRE PLANTER WILL BE GIVEN AWAY</div>

  <div class="promo-columns">
    <div class="feature">
      <h2 class="feature-title">FOOD GROWING<br>MACHINES</h2>
      <p class="feature-sub">Aeroponics Technology</p>
      <ul class="feature-list">
        <li><svg class="tick" viewBox="0 0 18 16"><path d="M2 8 L7 13 L16 2" fill="none" stroke="var(--green)" stroke-width="3.5" stroke-linecap="round" stroke-linejoin="round"/></svg>No soil</li>
        <li><svg class="tick" viewBox="0 0 18 16"><path d="M2 8 L7 13 L16 2" fill="none" stroke="var(--green)" stroke-width="3.5" stroke-linecap="round" stroke-linejoin="round"/></svg>No pesticides</li>
        <li><svg class="tick" viewBox="0 0 18 16"><path d="M2 8 L7 13 L16 2" fill="none" stroke="var(--green)" stroke-width="3.5" stroke-linecap="round" stroke-linejoin="round"/></svg>98% less water</li>
        <li><svg class="tick" viewBox="0 0 18 16"><path d="M2 8 L7 13 L16 2" fill="none" stroke="var(--green)" stroke-width="3.5" stroke-linecap="round" stroke-linejoin="round"/></svg>Grow year round</li>
      </ul>
    </div>
    <div class="divider"></div>
    <div class="feature">
      <h2 class="feature-title">FOOD GROWING<br>MACHINES</h2>
      <p class="feature-sub">Vertical Farming</p>
      <ul class="feature-list">
        <li><svg class="tick" viewBox="0 0 18 16"><path d="M2 8 L7 13 L16 2" fill="none" stroke="var(--green)" stroke-width="3.5" stroke-linecap="round" stroke-linejoin="round"/></svg>Urban Farming</li>
        <li><svg class="tick" viewBox="0 0 18 16"><path d="M2 8 L7 13 L16 2" fill="none" stroke="var(--green)" stroke-width="3.5" stroke-linecap="round" stroke-linejoin="round"/></svg>100% Organic</li>
        <li><svg class="tick" viewBox="0 0 18 16"><path d="M2 8 L7 13 L16 2" fill="none" stroke="var(--green)" stroke-width="3.5" stroke-linecap="round" stroke-linejoin="round"/></svg>Grows 40% Faster</li>
        <li><svg class="tick" viewBox="0 0 18 16"><path d="M2 8 L7 13 L16 2" fill="none" stroke="var(--green)" stroke-width="3.5" stroke-linecap="round" stroke-linejoin="round"/></svg>Indoors/outdoors</li>
      </ul>
    </div>
  </div>

  <div class="band band--bottom">FOLLOW US ON IG FOR A CHANCE TO WIN A SPIRE PLANTER</div>
</section>

<section class="card card--contact" aria-label="Contact side of business card">
  <svg class="contact-hero" viewBox="0 0 320 300">
    <defs>
      <linearGradient id="heroTone" x1="0" y1="0" x2="1" y2="1">
        <stop offset="0" stop-color="#8a7466"/>
        <stop offset=".45" stop-color="#d98aa8"/>
        <stop offset="1" stop-color="#6f9a58"/>
      </linearGradient>
    </defs>
    <path d="M0 0 H320 V96 C305 190 210 262 0 262 Z" fill="url(#heroTone)" role="img" aria-label="Photo of a young girl in a pink shirt picking chard from an indoor garden"/>
    <path d="M320 96 C305 190 210 262 0 262" fill="none" stroke="var(--leaf)" stroke-width="6"/>
    <path d="M320 112 C306 204 212 276 0 276" fill="none" stroke="var(--pink)" stroke-width="3"/>
  </svg>

  <div class="brand">
    <span class="brand-name">Brightleaf<br>Plots</span>
    <span class="brand-dot"></span>
  </div>

  <div class="person">
    <p class="person-name">Chef Morv</p>
    <p class="person-role">Owner</p>
  </div>

  <ul class="contact-list">
    <li>
      <svg class="contact-icon" viewBox="0 0 16 16"><path d="M4 1.5 L6.5 4.5 L5 6.5 C6 8.5 7.5 10 9.5 11 L11.5 9.5 L14.5 12 L12.5 14.5 C7 14 2 9 1.5 3.5 Z" fill="var(--pink)"/></svg>
      <span>: 555 417-3290</span>
    </li>
    <li>
      <svg class="contact-icon" viewBox="0 0 16 16"><circle cx="8" cy="8" r="6.5" fill="none" stroke="var(--pink)" stroke-width="1.6"/><ellipse cx="8" cy="8" rx="2.8" ry="6.5" fill="none" stroke="var(--pink)" stroke-width="1.3"/><path d="M1.5 8 H14.5" stroke="var(--pink)" stroke-width="1.3"/></svg>
      <span>: brightleafplots.example</span>
    </li>
    <li>
      <span class="contact-label">IG</span>
      <span>: brightleafplotsxy</span>
    </li>
  </ul>
</section>

</body>
</html>
```